Presenting a new Sci/Fi romance novel

Need a very attractive Facebook page design for a new novel
Striking, well-matched colors
Need only one of the pictures embedded, cropped to look best
Co-authors are Desmond K. Thornbury and Lydia R. Vantrescoe
Need to encourage readers to read for free with Novelo Boundless, or use link for paperback or e-book editions.

Sci-fi readers, literary romance readers, college and upward people

education, healthcare (teachers, therapists, students, professionals, sci/Fi enthusiasts)

Decorative

• "Perhaps it is never too late for love. Perhaps the universe is gracious. Perhaps there is hope after all. Or perhaps the ancients were right and our flaws usher us toward inevitable tragedy while we navigate our separate journeys together."
• A brilliant heading or structure or design scheme which will make it likely to be shared.

```html
<!DOCTYPE html>
<html lang="en">
<head>
<meta charset="utf-8">
<title>Harrow 3.0 — Page Cover</title>
<link rel="stylesheet" href="https://fonts.googleapis.com/css2?family=Kaushan+Script&family=Playfair+Display:wght@400&family=Poppins:wght@400;600;700&family=Allura&display=swap">
<style>
  :root {
    --page-bg: #6393f7;
    --night: #0b0705;
    --gold: #fcc531;
    --ink: #1b1203;
    --paper: #ffffff;
    --ember-1: #c9552a;
    --ember-2: #7d2f16;
  }
  * { margin: 0; padding: 0; box-sizing: border-box; }
  html, body { width: 1200px; height: 1200px; overflow: hidden; }
  body { background: var(--page-bg); position: relative; font-family: "Poppins", sans-serif; }

  .cover {
    position: absolute; left: 40px; top: 387px;
    width: 1120px; height: 425px; overflow: hidden;
    background: var(--night);
  }
  .cover-backdrop {
    position: absolute; inset: 0;
    background:
      radial-gradient(ellipse 260px 320px at 470px 150px, rgba(120,95,80,.55), transparent 70%),
      linear-gradient(90deg, #140d09 0%, #4a3a30 40%, #2a1f18 60%, #0d0806 80%, var(--night) 100%);
  }
  .book-stack {
    position: absolute; left: 46px; top: 29px; width: 322px; height: 377px;
    background: linear-gradient(160deg, var(--ember-1) 0%, #b44a22 45%, var(--ember-2) 100%);
    clip-path: polygon(0 7%, 70% 0, 100% 93%, 34% 100%, 7% 90%);
  }
  .title {
    position: absolute; left: 694px; top: 38px; width: 270px; text-align: center;
    font-family: "Kaushan Script", cursive; font-size: 54px; color: var(--paper);
    white-space: nowrap; line-height: 1.2;
  }
  .headline-perhaps {
    position: absolute; left: 578px; top: 110px;
    font-family: "Playfair Display", serif; font-size: 62px; color: var(--paper);
    letter-spacing: -2.5px; line-height: 1;
  }
  .headline-love {
    position: absolute; left: 850px; top: 110px;
    font-family: "Playfair Display", serif; font-size: 96px; color: var(--gold);
    letter-spacing: -4px; line-height: 1;
  }
  .headline-lead {
    position: absolute; left: 581px; top: 182px;
    font-size: 19px; color: var(--paper); letter-spacing: .2px; line-height: 1;
  }
  .blurb {
    position: absolute; left: 587px; top: 219px; width: 498px;
    font-size: 16.5px; line-height: 20.5px; color: var(--paper);
  }
  .blurb-line { display: block; text-align: justify; text-align-last: justify; white-space: nowrap; }
  .blurb-line:last-child { text-align-last: left; }
  .coauthors-label {
    position: absolute; left: 406px; top: 274px;
    font-weight: 700; font-size: 19px; color: var(--paper); letter-spacing: .5px; line-height: 1.3;
  }
  .signature {
    position: absolute; font-family: "Allura", cursive; color: var(--gold);
    font-size: 23px; line-height: 1; white-space: nowrap;
    transform: rotate(-12deg); transform-origin: left bottom;
  }
  .signature--first { left: 388px; top: 342px; }
  .signature--second { left: 394px; top: 382px; }
  .read-free {
    position: absolute; left: 653px; top: 340px;
    font-size: 13.5px; color: var(--paper);
  }
  .read-free svg { position: absolute; left: 168px; top: -2px; }
  .formats-band {
    position: absolute; left: 605px; top: 373px; width: 515px; height: 52px;
    background: var(--gold);
    clip-path: polygon(15px 0, 100% 0, 100% 100%, 0 100%);
    display: flex; align-items: center; justify-content: center; gap: 14px;
    padding-left: 20px;
    font-weight: 700; font-size: 18.5px; color: var(--ink); white-space: nowrap;
  }
</style>
</head>
<body>
  <section class="cover">
    <div class="cover-backdrop" role="img" aria-label="Dim photo of a shadowy figure behind dark curtains"></div>
    <div class="book-stack" role="img" aria-label="Stack of three copies of the novel, orange painted cover of a dancing couple beneath a tower"></div>

    <div class="title">Harrow 3.0</div>
    <div class="headline-perhaps">PERHAPS</div>
    <div class="headline-love">LOVE</div>
    <div class="headline-lead">IT IS NEVER TOO LATE FOR</div>
    <p class="blurb">
      <span class="blurb-line">Perhaps the universe is gracious. Perhaps there is hope</span>
      <span class="blurb-line">after all. Or perhaps the ancients were right and our flaws</span>
      <span class="blurb-line">usher us toward inevitable tragedy while we navigate our</span>
      <span class="blurb-line">separate journeys together.</span>
    </p>

    <div class="coauthors-label">CO-AUTHORS</div>
    <div class="signature signature--first">Desmond K. Thornbury</div>
    <div class="signature signature--second">Lydia R. Vantrescoe</div>

    <div class="read-free">Click here to read free
      <svg width="38" height="24" viewBox="0 0 38 24" fill="none" stroke="#fcc531" stroke-width="1.6" stroke-linecap="round">
        <path d="M2 8 C12 0, 24 2, 26 10 C27 16, 18 16, 22 10 C26 5, 32 10, 32 18"/>
        <path d="M28 15 L32 19 L35 14"/>
      </svg>
    </div>

    <div class="formats-band">
      <span>Novelo Boundless</span><span>|</span><span>get paperback</span><span>|</span><span>E-book</span>
    </div>
  </section>
</body>
</html>
```